Lumo Cellar Traders needs a new business card design

Colour theme: Gold + Red preferred
Front side: Main logo with my details as below;
Back side: Theme of some wine glasses or bottles, maybe different color of log together
Lumo Cellar Traders

Leo Park
박 성민 (this is Korean character) on the English typying board: qkr tjdals
Managing Director

Suite 7/5 Harlow Rd
Bayfield WA 6923
Tel) +61(8) 6027 3518
Mob) +61(412) 305 276

leo.park@lumocellartraders.example
lumocellar@lumocellartraders.example
www.lumocellartraders.example

Target Market(s)

Asian Market

Industry/Entity Type

Business

Contact Information for Business Card

Lumo Cellar Traders

Leo Park
박 성민 (this is Korean character) English typying: qkr tjdals
Managing Director

Suite 7/5 Harlow Rd
Bayfield WA 6923
Tel) +61(8) 6027 3518
Mob) +61(412) 305 276

Font styles to use
Serif
Decorative

Colors
ec1f27
f78f21
f04a50
faa54b
cadf82
abd036

Requirements
Must have
• Company Logo & wine theme
Nice to have
• Very simple & modern
Should not have
• No Red Color on the name of Leo Park or 박 성민
• No traditional looking. young and modern look preferred

```html
<!DOCTYPE html>
<html lang="en">
<head>
<meta charset="utf-8">
<title>Lumo Cellar Traders – Business Card</title>
<link rel="stylesheet" href="https://fonts.googleapis.com/css2?family=Exo+2:wght@400;500;600&family=Nanum+Gothic:wght@700&display=swap">
<style>
  :root {
    --page-bg: #efeae4;
    --card-white: #ffffff;
    --wine-red: #c81f30;
    --band-red: #c41c2c;
    --band-text: #7a0f18;
    --panel-light: #e2566a;
    --panel-mid: #d83a4c;
    --panel-deep: #c42236;
    --stripe-gold: #c99a3c;
    --stripe-dark: #9e1322;
    --cream-1: #fffdf8;
    --cream-2: #efe1c6;
    --ink-red: #8b1a22;
    --email-ink: #7d0f1c;
  }
  html, body {
    margin: 0;
    padding: 0;
    width: 1042px;
    height: 1200px;
    overflow: hidden;
    background: var(--page-bg);
    font-family: "Exo 2", "Segoe UI", sans-serif;
  }
  .canvas {
    position: relative;
    width: 1042px;
    height: 1200px;
  }
  .card {
    position: absolute;
    left: 62px;
    width: 918px;
    height: 510px;
    box-shadow: 0 6px 18px rgba(0,0,0,0.18);
    overflow: hidden;
  }
  .card-front {
    top: 69px;
    background: var(--card-white);
  }
  .brand {
    position: absolute;
    left: 200px;
    top: 230px;
    display: flex;
    align-items: center;
    gap: 22px;
  }
  .brand-dot {
    width: 92px;
    height: 92px;
    border-radius: 50%;
    background: var(--wine-red);
  }
  .brand-name {
    font-weight: 600;
    font-size: 60px;
    line-height: 1;
    color: var(--wine-red);
    letter-spacing: 1px;
    text-transform: uppercase;
  }
  .tagline-band {
    position: absolute;
    left: 0;
    right: 0;
    bottom: 0;
    height: 43px;
    background: var(--band-red);
    display: flex;
    align-items: center;
    justify-content: center;
  }
  .tagline {
    font-size: 19px;
    color: var(--band-text);
    letter-spacing: 0.5px;
  }
  .card-back {
    top: 621px;
    height: 500px;
  }
  .card-back svg {
    display: block;
  }
  .contact {
    position: absolute;
    left: 690px;
    top: 78px;
    width: 210px;
    text-align: center;
    color: var(--ink-red);
    font-weight: 500;
  }
  .contact p { margin: 0; }
  .contact-name { font-size: 23px; font-weight: 600; }
  .contact-name-ko { font-family: "Nanum Gothic", sans-serif; font-size: 22px; margin-top: 4px !important; }
  .contact-title { font-size: 20px; margin-top: 16px !important; }
  .contact-address { margin-top: 44px !important; font-size: 20px; line-height: 33px; }
</style>
</head>
<body>
<main class="canvas">

  <section class="card card-front" aria-label="Card front">
    <div class="brand">
      <span class="brand-dot" aria-hidden="true"></span>
      <span class="brand-name">Lumo Cellar Traders</span>
    </div>
    <div class="tagline-band">
      <span class="tagline">Connect &amp; Develop Your Business</span>
    </div>
  </section>

  <section class="card card-back" aria-label="Card back">
    <svg width="918" height="500" viewBox="0 0 918 500" xmlns="http://www.w3.org/2000/svg">
      <defs>
        <linearGradient id="cream" x1="0" y1="0" x2="1" y2="0">
          <stop offset="0" stop-color="var(--cream-2)"/>
          <stop offset="0.45" stop-color="var(--cream-1)"/>
          <stop offset="1" stop-color="var(--cream-2)"/>
        </linearGradient>
      </defs>
      <rect class="back-cream" width="918" height="500" fill="url(#cream)"/>
      <polygon class="back-panel" points="0,0 380,0 620,500 0,500" fill="var(--panel-light)"/>
      <polygon class="back-panel-mid" points="0,180 300,0 380,0 620,500 0,500" fill="var(--panel-mid)"/>
      <polygon class="back-triangle" points="120,500 405,40 610,500" fill="var(--panel-deep)"/>
      <polygon class="bottle-area" role="img" aria-label="Faint wine bottle silhouette" points="330,210 370,210 440,470 300,470" fill="#cf3044" opacity="0.5"/>
      <line class="stripe-dark" x1="392" y1="0" x2="630" y2="500" stroke="var(--stripe-dark)" stroke-width="12"/>
      <line class="stripe-gold" x1="378" y1="0" x2="616" y2="500" stroke="var(--stripe-gold)" stroke-width="5"/>
      <g class="emails" fill="var(--email-ink)" font-family="'Exo 2', sans-serif" font-size="17" transform="translate(95,470) rotate(-57)">
        <text x="0" y="0">leo.park@lumocellartraders.example</text>
        <text x="0" y="24">lumocellar@lumocellartraders.example</text>
        <text x="0" y="48">www.lumocellartraders.example</text>
      </g>
    </svg>
    <div class="contact">
      <p class="contact-name">Leo Park</p>
      <p class="contact-name-ko">박 성민</p>
      <p class="contact-title">Managing Director</p>
      <p class="contact-address">Suite 7/5 Harlow Rd<br>Bayfield WA 6923<br>Tel) +61(8) 6027 3518<br>Mob) +61(412) 305 276</p>
    </div>
  </section>

</main>
</body>
</html>
```